Business card design needed

We need a business card for a consulting company called Harbor Business Consulting which covers a range of business services in construction and Human Resources. We have chosen balck and red as the colours and have an idea for the logo of a person with arms outstretched signifying all encompassing. See attachment.
Industry/Entity Type
Construction
Contact Information for Business Card
Dalton Whitlow
Business Consultant/Project Manager/ Experienced Builder (Dip Bdg & Construction)
Mobile: 0482 613 954
Email: daltonwhitlow@harborconsulting.example.au
PO Box 5817
Kelvin Ridgeway, QLD, 4093, Australia
Logo Text
Harbor Business Consulting

```html
<!DOCTYPE html>
<html lang="en">
<head>
<meta charset="utf-8">
<title>Harbor Business Consulting – Business Card</title>
<link rel="stylesheet" href="https://fonts.googleapis.com/css2?family=PT+Sans:wght@400;700&family=PT+Sans+Narrow:wght@400;700&display=swap">
<style>
  :root {
    --blue-deep: #0b3f8f;
    --blue-mid: #1f6fc9;
    --blue-light: #cfe6fb;
    --red: #d4141c;
    --black: #0a0a0a;
    --white: #ffffff;
    --ink: #1a1a1a;
  }
  * { margin: 0; padding: 0; box-sizing: border-box; }
  html, body { width: 1200px; height: 631px; overflow: hidden; }
  body {
    position: relative;
    font-family: "PT Sans", Arial, sans-serif;
    background:
      radial-gradient(circle at 360px 300px, var(--white) 0, var(--blue-light) 110px, rgba(120,180,240,0.6) 260px, transparent 480px),
      linear-gradient(100deg, var(--blue-deep) 0%, var(--blue-mid) 40%, #5aa4ea 62%, var(--blue-mid) 100%);
  }

  /* Showcase brand mark */
  .brand-showcase {
    position: absolute; left: 200px; top: 130px; width: 340px;
    display: flex; flex-direction: column; align-items: center; gap: 22px;
  }
  .brand-dot { width: 220px; height: 220px; border-radius: 50%; background: var(--red); }
  .brand-name { font-size: 30px; font-weight: 700; color: var(--black); text-align: center; }

  /* Cards */
  .card { position: absolute; left: 690px; width: 508px; height: 292px; overflow: hidden; }
  .card-border {
    position: absolute; inset: 12px;
    border: 2px dashed var(--red);
    pointer-events: none;
  }

  /* Front */
  .card-front { top: 4px; background: var(--white); }
  .front-panel {
    position: absolute; right: 0; top: 0; width: 160px; height: 100%;
    background: linear-gradient(180deg, var(--black) 0%, var(--black) 30%, #6b6b6b 70%, var(--black) 100%);
    color: var(--white); text-align: center;
  }
  .front-fold { position: absolute; left: 304px; top: 0; width: 44px; height: 80px; }
  .panel-company { position: absolute; top: 28px; left: 10px; right: 10px; font-size: 13px; line-height: 1.3; }
  .panel-dot {
    position: absolute; left: 50%; top: 112px; width: 88px; height: 88px; margin-left: -44px;
    border-radius: 50%; background: var(--red);
  }
  .panel-tagline { position: absolute; top: 226px; left: 10px; right: 10px; font-size: 13px; line-height: 1.35; }

  .contact { position: absolute; left: 24px; top: 22px; width: 300px; color: var(--ink); }
  .contact-name { font-size: 36px; font-weight: 400; letter-spacing: 0.5px; margin-bottom: 14px; white-space: nowrap; }
  .contact-block { font-size: 12.5px; line-height: 16px; margin-bottom: 14px; white-space: nowrap; }

  /* Back */
  .card-back { top: 332px; background: var(--black); color: var(--white); font-family: "PT Sans Narrow", Arial, sans-serif; }
  .back-glow {
    position: absolute; left: 204px; top: 0; width: 100px; height: 100%;
    background: linear-gradient(90deg, transparent, rgba(180,180,180,0.55) 50%, transparent);
  }
  .back-title {
    position: absolute; left: 0; right: 0; top: 18px; text-align: center;
    font-size: 34px; font-weight: 700; letter-spacing: 0.5px; line-height: 40px;
  }
  .back-rule { position: absolute; left: 22px; right: 22px; top: 62px; height: 2px; background: var(--red); }
  .service-list { position: absolute; top: 78px; list-style: none; font-size: 15px; line-height: 27px; }
  .service-list.left { left: 24px; }
  .service-list.right { right: 24px; text-align: right; }
  .back-dot {
    position: absolute; left: 218px; top: 132px; width: 72px; height: 72px;
    border-radius: 50%; background: var(--red);
  }
</style>
</head>
<body>

  <div class="brand-showcase">
    <div class="brand-dot"></div>
    <div class="brand-name">Harbor Business Consulting</div>
  </div>

  <section class="card card-front">
    <div class="contact">
      <h1 class="contact-name">Dalton Whitlow</h1>
      <p class="contact-block">Business Consultant / Project Manager<br>Experienced Builder (Dip Bdg &amp; Construction)</p>
      <p class="contact-block">Mobile: 0482 613 954<br>E-mail: daltonwhitlow@harborconsulting.example.au</p>
      <p class="contact-block">PO Box 5817<br>Kelvin Ridgeway, QLD,<br>4093 Australia</p>
    </div>
    <div class="front-panel">
      <p class="panel-company">Harbor Business<br>Consulting Pty Ltd</p>
      <div class="panel-dot"></div>
      <p class="panel-tagline">'HELPING YOU<br>ACHIEVE'</p>
    </div>
    <svg class="front-fold" viewBox="0 0 44 80" aria-hidden="true">
      <polygon points="0,0 44,0 44,80" fill="var(--red)"/>
    </svg>
    <div class="card-border"></div>
  </section>

  <section class="card card-back">
    <div class="back-glow"></div>
    <h2 class="back-title">HARBOR BUSINESS CONSULTING</h2>
    <div class="back-rule"></div>
    <ul class="service-list left">
      <li>Construction Design Advice/Mgmt</li>
      <li>Building Site Supervision</li>
      <li>Bldg Maintenance Mgmt</li>
      <li>Project Management</li>
      <li>Estimating Services</li>
      <li>Subcontractor Mgmt</li>
      <li>Site Relocations</li>
    </ul>
    <div class="back-dot"></div>
    <ul class="service-list right">
      <li>Community/Sports Facilities</li>
      <li>Commercial/Industrial</li>
      <li>Multi-Unit Residential</li>
      <li>Educational Facilities</li>
      <li>Retail/Hospitality</li>
      <li>Medical/Health</li>
      <li>Domestic</li>
    </ul>
    <div class="card-border"></div>
  </section>

</body>
</html>
```